Business Card for Luxury Hospitality Industry Career Seeker

Need something Simple, Punctual, and Elegant.

Project goal is to update phone number, layout, and wording

I look forward to working with you to create a business card I can give to managers and employers in the Luxury Hospitality industry. I want to advance a career in this industry handing out cards to managers and directors on my way up.
Updates

Updated graphics preferences in brief - would like my name flanked by small Lion, Compass, & Rope and have the Halworth 5 Star logo on the back Added Saturday, January 14, 2017

Updated Brief:-Some wording has been removed-Card Front should be more simple and tidy now-Card Back word choice & flow is improved Added Sunday, January 15, 2017

Target Market(s)

Luxury Hospitality Industry Employers and Managers

Industry/Entity Type

Hospitality

Contact Information for Business Card

(Card Front)
Corbin T. Pellman (flanked by small Lion, Compass & Rope graphic)
Luxury Hospitality
555-317-8846
ridgefellow@mailvessel.example
netroster.example/in/corbin-pellman-vet-civ
My Experience = Our Success

(Card Back)
Graphic of: Halworth 5 Star logo and maybe QTR 5 Diamond Logo too
8 years military supply, logistics, & administrative experience
2 years intensive recruiting, marketing, and sales expertise
Adept problem solving, planning and management skills
5 Star, 5 Daimond, Luxury Hotels & Hospitality Rooms & Revenue

Requirements
Must have
• Name
• Phone Number
• Email Address
• Net Roster Address
• Slogan (My Experience = Our Success)
• Graphic on back: Halworth 5 Star logo
• Qualification Remarks
• Catchy logo
Nice to have
• Background that makes a viewer think Luxury Hospitality Experience and/or World Experience
• Color combinations I've seen & liked are black & yellow, black & white, and blue & white

```html
<!DOCTYPE html>
<html lang="en">
<head>
<meta charset="utf-8">
<title>Corbin T. Pellman – Business Card</title>
<link rel="stylesheet" href="https://fonts.googleapis.com/css2?family=Open+Sans:wght@400;600;700&family=Arimo:wght@400&display=swap">
<style>
  :root {
    --page: #e9e6e1;
    --card: #ffffff;
    --card-shade: #ececec;
    --blue: #2b8ac4;
    --blue-deep: #1f6fb0;
    --graphite: #4a4b4d;
    --ink: #6b6b6b;
    --emblem: #1a1a1a;
    --gold: #c9a646;
    --diamond: #2f5fb3;
  }
  * { margin: 0; padding: 0; box-sizing: border-box; }
  html, body { width: 1200px; height: 1023px; overflow: hidden; }
  body { background: var(--page); position: relative; font-family: "Open Sans", sans-serif; }

  .card {
    position: absolute;
    width: 700px; height: 400px;
    border-radius: 18px;
    background: linear-gradient(135deg, var(--card) 0%, var(--card) 55%, var(--card-shade) 100%);
    box-shadow: 0 3px 10px rgba(0,0,0,.18);
    overflow: hidden;
  }
  .card--front { left: 60px; top: 60px; }
  .card--back { left: 440px; top: 570px; }

  /* front */
  .emblem {
    position: absolute; left: 50px; top: 95px;
    width: 190px; height: 170px;
    border-radius: 50%;
    background: radial-gradient(circle, #3a3a3a 0%, var(--emblem) 70%);
  }
  .divider {
    position: absolute; left: 282px; top: 70px;
    width: 1px; height: 190px; background: var(--blue);
  }
  .identity { position: absolute; left: 300px; top: 60px; }
  .identity__name {
    font-weight: 600; font-size: 40px; color: var(--blue); letter-spacing: 1px; line-height: 1.1;
  }
  .identity__title { font-size: 19px; color: var(--ink); margin-top: 2px; }
  .contacts { list-style: none; margin-top: 22px; }
  .contacts li {
    display: flex; align-items: center; gap: 12px;
    font-size: 15px; color: var(--ink); letter-spacing: .6px; margin-bottom: 9px;
  }
  .contacts svg { width: 16px; height: 16px; flex: none; }
  .contacts .accent { color: var(--blue); }
  .band {
    position: absolute; left: 0; bottom: 0; width: 100%; height: 52px;
  }
  .band__slogan {
    position: absolute; left: 40px; bottom: 15px;
    font-family: "Arimo", sans-serif; font-size: 18px; color: #fff;
  }

  /* back */
  .badge-diamond {
    position: absolute; left: 40px; top: 40px;
    width: 200px; height: 90px; border-radius: 12px;
    background: linear-gradient(180deg, #5a82c9, var(--diamond));
  }
  .qualifications { position: absolute; left: 40px; top: 158px; list-style: none; }
  .qualifications li {
    display: flex; align-items: center; gap: 12px;
    font-family: "Arimo", sans-serif; font-size: 17px; color: var(--blue-deep);
    margin-bottom: 9px; letter-spacing: .2px;
  }
  .qualifications svg { width: 14px; height: 14px; flex: none; }
  .badge-stars {
    position: absolute; right: 40px; bottom: 30px;
    width: 180px; height: 110px; border-radius: 50%;
    background: radial-gradient(circle, #e0c878, var(--gold));
  }
</style>
</head>
<body>

<section class="card card--front">
  <div class="emblem" role="img" aria-label="Lion, Compass &amp; Rope emblem"></div>
  <div class="divider"></div>
  <div class="identity">
    <h1 class="identity__name">Corbin T. Pellman</h1>
    <p class="identity__title">Title</p>
    <ul class="contacts">
      <li>
        <svg viewBox="0 0 16 16"><circle cx="8" cy="8" r="7" fill="none" stroke="var(--blue)" stroke-width="1.5"/><path d="M5.5 4.5l1.5 1.5-1 1a5 5 0 0 0 3 3l1-1 1.5 1.5-1 1.2C7.5 12 4 8.5 4.3 5.5z" fill="var(--blue)"/></svg>
        555-317-8846
      </li>
      <li>
        <svg viewBox="0 0 16 16"><rect x="1" y="3" width="14" height="10" fill="var(--blue)"/><path d="M1 3l7 6 7-6" fill="none" stroke="#fff" stroke-width="1.2"/></svg>
        ridgefellow@mailvessel.example
      </li>
      <li>
        <svg viewBox="0 0 16 16" fill="none" stroke="var(--blue)" stroke-width="1.2"><circle cx="8" cy="8" r="7"/><ellipse cx="8" cy="8" rx="3" ry="7"/><path d="M1 8h14M2.5 4.5h11M2.5 11.5h11"/></svg>
        <span>www.<span class="accent">yoursite</span>.example</span>
      </li>
      <li>
        <svg viewBox="0 0 16 16"><circle cx="8" cy="8" r="7" fill="var(--blue)"/></svg>
        netroster.example/in/corbin-pellman-vet-civ
      </li>
    </ul>
  </div>
  <svg class="band" viewBox="0 0 700 52" preserveAspectRatio="none">
    <polygon points="0,0 520,0 505,52 0,52" fill="var(--blue)"/>
    <polygon points="535,0 700,0 700,52 520,52" fill="var(--graphite)"/>
  </svg>
  <p class="band__slogan">My Experience = Our Success</p>
</section>

<section class="card card--back">
  <div class="badge-diamond" role="img" aria-label="QTR 5 Diamond award badge"></div>
  <ul class="qualifications">
    <li><svg viewBox="0 0 14 14"><path d="M2 8l3 3 7-9" fill="none" stroke="var(--blue-deep)" stroke-width="2.2"/></svg>8 years military supply, logistics, &amp; administrative experience</li>
    <li><svg viewBox="0 0 14 14"><path d="M2 8l3 3 7-9" fill="none" stroke="var(--blue-deep)" stroke-width="2.2"/></svg>2 years intensive recruiting, marketing, and sales expertise</li>
    <li><svg viewBox="0 0 14 14"><path d="M2 8l3 3 7-9" fill="none" stroke="var(--blue-deep)" stroke-width="2.2"/></svg>Adept problem solving, planning and management skills</li>
    <li><svg viewBox="0 0 14 14"><path d="M2 8l3 3 7-9" fill="none" stroke="var(--blue-deep)" stroke-width="2.2"/></svg>5 Star, 5 Daimond, Luxury Hotels &amp; Hospitality Rooms &amp; Revenue</li>
  </ul>
  <div class="badge-stars" role="img" aria-label="Halworth 5 Star badge"></div>
</section>

</body>
</html>
```